Swimming Pool Supply Company Business Cards

We need business cards designed for company. These need to be easy to edit so that we can fill in names, titles, and contact info for each person who works here.

Dalton R. Whitfield
Manager of Legal & Finance
K.L. Brisbane, Incorporated

4837 Grenway Avenue
Marlow Heights, PA 19243

E. dalton@klbrisbane-example.com
M. (215) 555-0173
O. (215) 555-0148

Contact Information for Business Card

Looking to upgrade current business cards with graphic that can be edited. Looking for fresh ideas for an age old industry.

Font styles to use
Serif
Sans Serif

Colors

Designer to choose colors to be used in the design.

Requirements
Must have
• Professional, fresh, unique but professional

```html
<!DOCTYPE html>
<html lang="en">
<head>
<meta charset="utf-8">
<title>K.L. Brisbane Business Cards</title>
<link href="https://fonts.googleapis.com/css2?family=Open+Sans:wght@400;700;800&display=swap" rel="stylesheet">
<style>
  :root {
    --page-bg: #ecebe8;
    --card-dark: #1b1b1c;
    --card-dark-edge: #2c2c2e;
    --card-light: #fbfbfb;
    --ink-light: #f2f2f2;
    --ink-muted: #d6d6d6;
    --ink-dark: #141414;
    --ink-tag: #2a2a2a;
  }
  * { box-sizing: border-box; margin: 0; padding: 0; }
  html, body {
    width: 1200px; height: 950px; overflow: hidden;
    background: var(--page-bg);
    font-family: "Open Sans", Arial, sans-serif;
  }
  .sheet {
    position: relative; width: 1200px; height: 950px;
    display: flex; flex-direction: column; align-items: center; justify-content: center; gap: 70px;
  }
  .card {
    width: 630px; height: 360px; position: relative;
    box-shadow: 0 10px 26px rgba(0,0,0,.18);
  }
  .card--front {
    background: linear-gradient(135deg, var(--card-dark-edge) 0%, var(--card-dark) 55%);
    color: var(--ink-light);
  }
  .identity {
    position: absolute; top: 34px; right: 38px; text-align: right;
  }
  .identity__name {
    font-weight: 700; font-size: 22px; letter-spacing: .5px; text-transform: uppercase;
  }
  .identity__role, .identity__company {
    font-size: 15.5px; color: var(--ink-muted); line-height: 1.35;
  }
  .contact {
    position: absolute; left: 38px; bottom: 30px;
    font-size: 15.5px; line-height: 1.4; color: var(--ink-muted); list-style: none;
  }
  .contact__row { display: flex; align-items: center; gap: 8px; }
  .contact__icon { width: 14px; height: 14px; flex: none; fill: var(--ink-light); }
  .contact__address { margin-bottom: 2px; }
  .card--back {
    background: var(--card-light);
    display: flex; flex-direction: column; align-items: center; justify-content: center;
  }
  .brand__name {
    font-weight: 800; font-size: 74px; letter-spacing: 2px; color: var(--ink-dark); line-height: 1;
  }
  .brand__tagline {
    margin-top: 14px; font-size: 16px; color: var(--ink-tag);
  }
</style>
</head>
<body>
<main class="sheet">
  <section class="card card--front" aria-label="Business card front">
    <div class="identity">
      <p class="identity__name">Dalton R. Whitfield</p>
      <p class="identity__role">Manager of Legal &amp; Finance</p>
      <p class="identity__company">K.L. Brisbane, Incorporated</p>
    </div>
    <ul class="contact">
      <li class="contact__address">4837 Grenway Avenue<br>Marlow Heights, PA 19243</li>
      <li class="contact__row">
        <svg class="contact__icon" viewBox="0 0 14 14" aria-hidden="true"><path d="M3 1h2.5l1 3-1.5 1a7 7 0 0 0 4 4l1-1.5 3 1V11a2 2 0 0 1-2 2A11 11 0 0 1 1 3a2 2 0 0 1 2-2z"/></svg>
        (215) 555-0148
      </li>
      <li class="contact__row">
        <svg class="contact__icon" viewBox="0 0 14 14" aria-hidden="true"><path d="M4 0h6a1 1 0 0 1 1 1v12a1 1 0 0 1-1 1H4a1 1 0 0 1-1-1V1a1 1 0 0 1 1-1zm0.5 1.5v9.5h5V1.5z"/></svg>
        (215) 555-0173
      </li>
      <li class="contact__row">
        <svg class="contact__icon" viewBox="0 0 14 14" aria-hidden="true"><path d="M1 3h12v8H1zm1 1v.3l5 3.4 5-3.4V4z"/></svg>
        dalton@klbrisbane-example.com
      </li>
      <li class="contact__row">
        <svg class="contact__icon" viewBox="0 0 14 14" aria-hidden="true"><circle cx="7" cy="7" r="6.5"/><path d="M1 7h12M7 .5c-2.5 3-2.5 10 0 13M7 .5c2.5 3 2.5 10 0 13" stroke="#1b1b1c" stroke-width="1" fill="none"/></svg>
        www.klbrisbane-example.com
      </li>
    </ul>
  </section>

  <section class="card card--back" aria-label="Business card back">
    <p class="brand__name">BRISBANE</p>
    <p class="brand__tagline">Big Enough to Serve You, Small Enough to Care</p>
  </section>
</main>
</body>
</html>
```